We are looking for a clean new looking business card.

We would like a new, clean, and modern type business card with our updated contact information. We are a small a plumbing and heating and gasfitting company who offer 24 hr emergency service as well.
We feel our logo looks best on a white background.
Our current cards are outdated, both the design and the information.

Industry/Entity Type

Plumbing and heating

Contact Information for Business Card

Logo, Name, Title, Phone#, Email, Website, "24/7 Emergency Service"

Colors
0054AA
0677BA
7BADD7
CADEEF
E8F1F8

```html
<!DOCTYPE html>
<html lang="en">
<head>
<meta charset="utf-8">
<title>Clearwell Business Card</title>
<link rel="stylesheet" href="https://fonts.googleapis.com/css2?family=Open+Sans:wght@400;600;700&display=swap">
<style>
  :root {
    --navy: #0054AA;
    --blue: #0677BA;
    --sky: #7BADD7;
    --mist: #CADEEF;
    --ice: #E8F1F8;
    --back: #1592C7;
    --ink: #55595e;
    --white: #ffffff;
    --stage: #d9d9d7;
  }
  * { box-sizing: border-box; margin: 0; padding: 0; }
  html, body { width: 1200px; height: 801px; overflow: hidden; }
  body {
    background: var(--stage);
    font-family: "Open Sans", Arial, sans-serif;
    display: flex;
    align-items: center;
    justify-content: center;
    gap: 40px;
  }
  .card {
    width: 540px;
    height: 309px;
    position: relative;
    border-bottom: 3px solid var(--blue);
    box-shadow: 0 6px 18px rgba(0,0,0,0.18);
  }
  .card-front { background: var(--white); }
  .card-back { background: var(--back); border-bottom-color: var(--navy); display: flex; align-items: center; justify-content: center; }

  .brand {
    position: absolute;
    left: 30px;
    top: 110px;
    width: 230px;
    display: flex;
    align-items: center;
    justify-content: center;
    gap: 10px;
  }
  .brand-dot { width: 22px; height: 22px; border-radius: 50%; background: var(--blue); }
  .brand-name { font-size: 38px; font-weight: 700; color: var(--blue); letter-spacing: 0.5px; }

  .divider {
    position: absolute;
    left: 282px;
    top: 62px;
    width: 1px;
    height: 118px;
    background: var(--blue);
  }
  .contact {
    position: absolute;
    left: 300px;
    top: 58px;
  }
  .person-name { font-size: 19px; font-weight: 700; color: var(--navy); letter-spacing: 0.3px; }
  .person-title { font-size: 15px; color: var(--ink); margin-bottom: 10px; }
  .contact-list { list-style: none; }
  .contact-item { display: flex; align-items: center; gap: 7px; font-size: 14px; color: var(--ink); line-height: 21px; }
  .contact-icon { width: 11px; height: 11px; fill: var(--blue); flex: none; }

  .tagline {
    position: absolute;
    left: 282px;
    bottom: 52px;
    font-size: 16px;
    font-weight: 600;
    color: var(--navy);
  }
  .back-mark { width: 140px; height: 140px; border-radius: 50%; background: var(--blue); box-shadow: inset 0 2px 4px rgba(0,0,0,0.15); }
</style>
</head>
<body>
  <section class="card card-front">
    <div class="brand">
      <span class="brand-dot"></span>
      <span class="brand-name">clearwell</span>
    </div>
    <div class="divider"></div>
    <div class="contact">
      <p class="person-name">DANA WHITLOCK</p>
      <p class="person-title">President</p>
      <ul class="contact-list">
        <li class="contact-item">
          <svg class="contact-icon" viewBox="0 0 12 12"><path d="M2.5 0.5 L4.5 0.5 L5.2 3.2 L3.8 4.3 C4.5 5.8 6.2 7.5 7.7 8.2 L8.8 6.8 L11.5 7.5 L11.5 9.5 C11.5 10.6 10.6 11.5 9.5 11.5 C4.5 11.5 0.5 7.5 0.5 2.5 C0.5 1.4 1.4 0.5 2.5 0.5 Z"/></svg>
          555-014-2290
        </li>
        <li class="contact-item">
          <svg class="contact-icon" viewBox="0 0 12 12"><path d="M0.5 2.5 H11.5 V9.5 H0.5 Z M0.5 2.5 L6 6.5 L11.5 2.5" stroke="var(--white)" stroke-width="0.8"/></svg>
          dana@clearwellpro.com
        </li>
        <li class="contact-item">
          <svg class="contact-icon" viewBox="0 0 12 12"><circle cx="6" cy="6" r="5.5"/><path d="M0.5 6 H11.5 M6 0.5 C3.5 3 3.5 9 6 11.5 M6 0.5 C8.5 3 8.5 9 6 11.5" stroke="var(--white)" stroke-width="0.8" fill="none"/></svg>
          www.clearwellpro.com
        </li>
      </ul>
    </div>
    <p class="tagline">"24/7 EMERGENCY SERVICE"</p>
  </section>

  <section class="card card-back">
    <div class="back-mark"></div>
  </section>
</body>
</html>
```